Wendlow Cellars -responsive, bootstrap website design

Looking to build a responsive service website.

Logo and pictures have been provided.

PLEASE REVIEW ATTACHED DESIGN STYLE GUIDES & CLIENT CREATIVE BRIEF FOR OUR REQUIREMENT. THANK YOU AND GOOD LUCK!

```html
<!DOCTYPE html>
<html lang="en">
<head>
<meta charset="utf-8">
<title>Wendlow Cellars</title>
<link href="https://fonts.googleapis.com/css2?family=Oranienbaum&family=Arimo:ital,wght@0,400;0,700;1,400&family=Great+Vibes&display=swap" rel="stylesheet">
<style>
:root{
  --ink:#000;
  --night:#0b0b0b;
  --char:#1a1a1a;
  --smoke:#2a2a2a;
  --line:#5a5a5a;
  --silver:#bdbdbd;
  --paper:#f2f2f2;
  --muted:#9a9a9a;
  --sepia:#7a5a3a;
  --parchment:#8a6a44;
}
*{margin:0;padding:0;box-sizing:border-box}
html,body{width:1200px;height:2752px;overflow:hidden;background:var(--ink)}
body{position:relative;font-family:"Arimo",Arial,sans-serif;color:var(--paper)}
.abs{position:absolute}
.display{font-family:"Oranienbaum",Georgia,serif;text-transform:uppercase;letter-spacing:1px}

/* header */
.site-header{left:0;top:0;width:1200px;height:215px;background:linear-gradient(#1c1c1c,#0e0e0e)}
.site-header::after{content:"";position:absolute;left:0;right:0;top:196px;height:6px;border-top:2px solid #6a6a6a;border-bottom:1px solid #3a3a3a}
.brand{left:523px;top:18px;width:150px;height:116px;border:3px solid #6c6c6c;border-radius:10px;background:#111;display:flex;flex-direction:column;align-items:center;justify-content:center;gap:6px}
.brand-name{font-family:"Oranienbaum",Georgia,serif;font-size:27px;line-height:1;color:var(--paper);text-align:center}
.brand-tag{font-size:7px;letter-spacing:2px;color:var(--silver);text-transform:uppercase}
.account{left:776px;top:121px;font-size:10px;color:var(--silver);text-transform:uppercase;display:flex;gap:14px;align-items:center}
.main-nav{left:0;top:166px;width:1200px;height:20px}
.main-nav a{position:absolute;font-size:13px;color:var(--paper);text-decoration:none;text-transform:uppercase;letter-spacing:.5px}

/* hero */
.hero{left:0;top:215px;width:1200px;height:383px;background:linear-gradient(100deg,#6b5b4c 0%,#d9cdbb 35%,#a89482 60%,#efe6da 85%,#8a7a6a 100%)}
.hero-badge{left:697px;top:336px;width:265px;height:170px;background:#0c0c0c;border:2px solid #000;display:flex;align-items:center;justify-content:center}
.hero-badge::before{content:"";position:absolute;inset:8px;border:1px solid #444}
.hero-badge .brand-name{font-size:38px;color:#8a8a8a}
.slider-arrows{left:958px;top:550px;display:flex;gap:3px}
.slider-arrows span{width:22px;height:23px;background:#2a2a2a;display:flex;align-items:center;justify-content:center}

/* pillars */
.pillars-band{left:0;top:598px;width:1200px;height:378px;background:radial-gradient(ellipse at 50% 40%,#2c2c2c,#141414 70%)}
.pillars-panel{left:172px;top:637px;width:856px;height:295px;background:var(--ink);border:1px solid #333}
.pillar{position:absolute;top:30px;width:242px}
.pillar h3{font-size:25px;color:var(--silver);font-weight:400;margin-bottom:8px}
.pillar .photo{width:242px;height:130px}
.pillar ul{list-style:none;margin-top:16px}
.pillar li{font-size:11px;color:var(--paper);margin-bottom:11px;padding-left:14px;position:relative}
.pillar li::before{content:"›";position:absolute;left:0;top:-2px;color:var(--muted);font-size:13px}

/* club */
.club-band{left:0;top:976px;width:1200px;height:483px;background:radial-gradient(ellipse at 50% 45%,#4a3220 0%,#2a1c12 55%,#120c08 100%)}
.club-card{left:229px;top:1092px;width:740px;height:260px;background:linear-gradient(135deg,#8f7150,#6e5236 60%,#7d6244);border:2px solid #a98d6c}
.club-card::before{content:"";position:absolute;inset:8px;border:1px solid rgba(230,210,180,.5)}
.section-title{display:flex;align-items:center;justify-content:center;gap:14px}
.section-title .rule{height:3px;border-top:1px solid currentColor;border-bottom:1px solid currentColor;opacity:.7}
.section-title h2{font-size:26px;font-weight:400;color:var(--paper)}
.club-title{left:0;top:32px;width:740px;color:#e8d8c0}
.club-col{position:absolute;top:98px;width:145px}
.club-col h4{font-size:10px;font-weight:400;line-height:19px;text-transform:uppercase;padding-bottom:6px;border-bottom:1px solid rgba(240,225,200,.6);margin-bottom:12px}
.club-col p{font-size:10px;font-style:italic;line-height:20px;color:#f2e8da}

/* purchase */
.purchase-band{left:0;top:1459px;width:1200px;height:528px;background:radial-gradient(ellipse at 30% 60%,#3a332e,#1e1a17 50%,#0e0c0b 100%)}
.purchase-title{left:312px;top:1578px;width:628px;color:#8a8a8a}
.purchase-photo{left:217px;top:1644px;width:189px;height:226px;background:#fff;padding:7px}
.purchase-photo div{width:100%;height:100%;background:linear-gradient(120deg,#cfc5b8,#6e6158 55%,#2a2320)}
.purchase-copy{left:437px;top:1655px;width:512px}
.purchase-copy h3{font-size:14px;font-weight:400;text-transform:uppercase;margin-bottom:13px}
.purchase-copy p{font-size:10.5px;line-height:21px;color:#e6e6e6}
.btn{display:inline-block;margin-top:22px;border:1px solid #777;background:#1b1b1b;color:var(--silver);font-size:12px;padding:9px 18px;text-transform:uppercase}

/* dealer */
.dealer-band{left:0;top:1987px;width:1200px;height:678px;background:linear-gradient(#2e2e2e,#4a4a4a 30%,#1c1c1c 70%,#3a3a3a)}
.dealer-panel{left:228px;top:2055px;width:745px;height:547px;background:var(--ink);border:1px solid #2c2c2c}
.dealer-title{left:0;top:30px;width:745px;color:#555}
.dealer-title h2{color:#9a9a9a}
.dealer-col{position:absolute;top:108px;width:307px}
.dealer-col .photo{height:183px}
.dealer-col h3{font-size:24px;font-weight:400;color:var(--paper);margin:35px 0 14px}
.dealer-col p{font-size:10px;line-height:22px;color:#cfcfcf;margin-bottom:14px}

/* footer */
.site-footer{left:0;top:2665px;width:1200px;height:87px;background:linear-gradient(#121212,#060606);border-top:1px solid #2a2a2a}
.copyright{left:174px;top:2707px;font-size:9px;color:var(--muted);text-transform:uppercase}
.social-label{left:683px;top:2692px;font-family:"Great Vibes",cursive;font-size:22px;color:#777}
.social{left:906px;top:2693px;display:flex;gap:14px}
.social span{width:32px;height:32px;border:1px solid #3a3a3a;background:#161616}
</style>
</head>
<body>

<header class="abs site-header">
  <div class="abs brand"><span class="brand-name">Wendlow Cellars</span><span class="brand-tag">Ferren Creek Valley</span></div>
  <div class="abs account">
    <span>My Account</span>
    <span style="display:flex;align-items:center;gap:6px">
      <svg width="14" height="12" viewBox="0 0 14 12"><path d="M0 1h3l2 7h7l2-5H4" fill="none" stroke="#bdbdbd" stroke-width="1.2"/><circle cx="6" cy="10.5" r="1" fill="#bdbdbd"/><circle cx="11" cy="10.5" r="1" fill="#bdbdbd"/></svg>
      Your Cart Is : 0 Items
    </span>
  </div>
  <nav class="abs main-nav">
    <a style="left:235px">Wines Story</a>
    <a style="left:385px">Shop Wine</a>
    <a style="left:525px">Gallery</a>
    <a style="left:651px">News</a>
    <a style="left:761px">Blog</a>
    <a style="left:870px">Dealer Location</a>
  </nav>
</header>

<section class="abs hero" role="img" aria-label="Sepia photo of a glass of red wine beside a bottle"></section>
<div class="abs hero-badge"><span class="brand-name">Wendlow Cellars</span></div>
<div class="abs slider-arrows">
  <span><svg width="8" height="10"><path d="M6 1L2 5l4 4" fill="none" stroke="#ddd" stroke-width="1.5"/></svg></span>
  <span><svg width="8" height="10"><path d="M2 1l4 4-4 4" fill="none" stroke="#ddd" stroke-width="1.5"/></svg></span>
</div>

<section class="abs pillars-band"></section>
<div class="abs pillars-panel">
  <div class="pillar" style="left:32px">
    <h3 class="display">Family</h3>
    <div class="photo" role="img" aria-label="Couple toasting with wine glasses" style="background:linear-gradient(120deg,#8a2a4a,#c25a6a 45%,#3a1420)"></div>
    <ul><li>Handcrafted</li><li>Small batch winery</li></ul>
  </div>
  <div class="pillar" style="left:305px">
    <h3 class="display">Tradition</h3>
    <div class="photo" role="img" aria-label="Rows of oak wine barrels" style="background:linear-gradient(160deg,#e0a040,#b06018 50%,#5a2a08)"></div>
    <ul><li>Handcrafted</li><li>Small batch winery</li></ul>
  </div>
  <div class="pillar" style="left:580px">
    <h3 class="display">Wendlow</h3>
    <div class="photo" role="img" aria-label="Stacked wine bottles lying in a rack" style="background:linear-gradient(150deg,#2a3a2a,#a8a090 45%,#5a2a2a 70%,#1a1a1a)"></div>
    <ul><li>Handcrafted</li><li>Small batch winery</li></ul>
  </div>
</div>

<section class="abs club-band" role="img" aria-label="Brick cellar vault with wine barrels"></section>
<div class="abs club-card">
  <div class="abs section-title club-title"><span class="rule" style="width:130px"></span><h2 class="display">Join Our Wine Club</h2><span class="rule" style="width:130px"></span></div>
  <div class="club-col" style="left:30px"><h4>Lorem ipsum is simply dummy text</h4><p>Lorem Ipsum is simply dummy text of the printing and typesetting industry. Lorem Ipsum has been the industry's...</p></div>
  <div class="club-col" style="left:208px"><h4>Lorem ipsum is simply dummy text</h4><p>Lorem Ipsum is simply dummy text of the printing and typesetting industry. Lorem Ipsum has been the industry's...</p></div>
  <div class="club-col" style="left:388px"><h4>Lorem ipsum is simply dummy text</h4><p>Lorem Ipsum is simply dummy text of the printing and typesetting industry. Lorem Ipsum has been the industry's...</p></div>
  <div class="club-col" style="left:566px"><h4>Lorem ipsum is simply dummy text</h4><p>Lorem Ipsum is simply dummy text of the printing and typesetting industry. Lorem Ipsum has been the industry's...</p></div>
</div>

<section class="abs purchase-band" role="img" aria-label="Dark blurred close-up of wine glasses"></section>
<div class="abs section-title purchase-title"><span class="rule" style="width:228px"></span><h2 class="display">Purchase</h2><span class="rule" style="width:294px"></span></div>
<div class="abs purchase-photo"><div role="img" aria-label="Glass of red wine beside a bottle"></div></div>
<div class="abs purchase-copy">
  <h3>Lorem ipsum is simply dummy text of the printing</h3>
  <p>Lorem Ipsum is simply dummy text of the printing and typesetting industry. Lorem Ipsum has been the industry's standard dummy text ever since the 1500s, when an unknown printer took a galley of type and scrambled it to make a type specimen book. It has survived not only five centuries, but also the leap into electronic typesetting, remaining essentially unchanged. It was popularised in the 1960s with the release of Letraset sheets containing Lorem Ipsum passages, and more recently with desktop publishing software...</p>
  <span class="btn">Purchase</span>
</div>

<section class="abs dealer-band" role="img" aria-label="Monochrome table scene with a wine bottle and glasses"></section>
<div class="abs dealer-panel">
  <div class="abs section-title dealer-title"><span class="rule" style="width:130px"></span><h2 class="display">Find a Dealer</h2><span class="rule" style="width:190px"></span></div>
  <div class="dealer-col" style="left:44px">
    <div class="photo" role="img" aria-label="Wine bar with glasses and bottle shelves" style="background:linear-gradient(150deg,#3a2410,#c08040 45%,#5a3018 75%,#1a0e06)"></div>
    <h3 class="display">Find Our Wines</h3>
    <p>Lorem Ipsum is simply dummy text of the printing and typesetting industry. Lorem Ipsum has been the industry's standard dummy text ever since the 1500s, when an unknown printer took a galley of type and scrambled it to make a type specimen book.</p>
    <p>when an unknown printer took a galley of type and scrambled it to make a type specimen book.</p>
  </div>
  <div class="dealer-col" style="left:394px">
    <div class="photo" role="img" aria-label="Wine corks with grape leaves" style="background:linear-gradient(150deg,#6a2a20,#c8a878 45%,#5a7a30 70%,#3a2018)"></div>
    <h3 class="display">Trade and Media</h3>
    <p>Lorem Ipsum is simply dummy text of the printing and typesetting industry. Lorem Ipsum has been the industry's standard dummy text ever since the 1500s, when an unknown printer took a galley of type and scrambled it to make a type specimen book.</p>
    <p>when an unknown printer took a galley of type and scrambled it to make a type specimen book.</p>
  </div>
</div>

<footer class="abs site-footer"></footer>
<div class="abs copyright">© 2014 - Wendlow - All Rights Reserved</div>
<div class="abs social-label">Connect with our social network :</div>
<div class="abs social" aria-label="Social network links"><span></span><span></span><span></span></div>

</body>
</html>
```